Business Card Design

this is a new company aimed at the automotive glass industry
what we do is repair cracked windscreens its based in western austraila
I like the old dragracing signwritting logos
I want it to stand out thats why ive gone with the name and title
I dont have a logo but if you can think of one that would be great
but not essential
on the back of the business card i would like Quicker Cheaper Better

Target Market(s)

automotive (car yards ,car auctions , trucking companys ect )

Industry/Entity Type

Automotive

Contact Information for Business Card

Pane Rangers ,
Glass Crack repair specialists ,
Darren Whitlock ,0438 162 705 ,dwhitlock@paneriderswa.com.au

```html
<!DOCTYPE html>
<html lang="en">
<head>
<meta charset="utf-8">
<title>Pane Rangers – Business Card</title>
<link href="https://fonts.googleapis.com/css2?family=Saira+Condensed:wght@700&display=swap" rel="stylesheet">
<style>
  :root {
    --stage: #1c1c1c;
    --ink: #1a1a1a;
    --ink-soft: #333333;
    --accent-red: #e0231c;
    --silver-light: #e6e7e8;
    --silver-mid: #bfc1c3;
    --silver-dark: #8e9092;
    --glass-light: #e4ece8;
    --glass-mid: #b9cbc4;
    --glass-dark: #8fa9a1;
    --band: #ffffff;
    --band-edge: #eeeeee;
  }
  * { margin: 0; padding: 0; box-sizing: border-box; }
  html, body {
    width: 1200px;
    height: 871px;
    overflow: hidden;
    background: var(--stage);
  }
  .canvas {
    position: relative;
    width: 1200px;
    height: 871px;
    display: flex;
    align-items: center;
    justify-content: center;
    gap: 40px;
    font-family: "Saira Condensed", "Arial Narrow", sans-serif;
    font-weight: 700;
  }
  .card {
    position: relative;
    width: 540px;
    height: 309px;
    overflow: hidden;
    box-shadow: 0 10px 30px rgba(0,0,0,0.6);
  }
  .card-texture {
    position: absolute;
    inset: 0;
  }

  /* Brand side */
  .card--front .card-texture {
    background: radial-gradient(ellipse at 60% 20%, var(--silver-light) 0%, var(--silver-mid) 55%, var(--silver-dark) 100%);
  }
  .brand {
    position: absolute;
    left: 0;
    right: 0;
    top: 92px;
    text-align: center;
  }
  .brand-name {
    font-size: 54px;
    line-height: 1;
    letter-spacing: 8px;
    color: var(--ink-soft);
  }
  .brand-specialty {
    margin-top: 12px;
    font-size: 17px;
    line-height: 1;
    letter-spacing: 5px;
    color: var(--ink-soft);
  }
  .brand-tagline {
    margin-top: 16px;
    font-size: 19px;
    line-height: 1;
    letter-spacing: 5px;
    word-spacing: 14px;
    color: var(--accent-red);
  }

  /* Contact side */
  .card--back .card-texture {
    background: linear-gradient(160deg, var(--glass-light) 0%, var(--glass-mid) 55%, var(--glass-dark) 100%);
  }
  .contact-band {
    position: absolute;
    left: 0;
    right: 0;
    top: 68px;
    height: 132px;
    background: linear-gradient(180deg, var(--band) 0%, var(--band-edge) 100%);
    box-shadow: 0 3px 8px rgba(0,0,0,0.25);
  }
  .contact {
    position: absolute;
    left: 0;
    right: 0;
    top: 82px;
    text-align: center;
  }
  .contact-name {
    font-size: 24px;
    line-height: 1.1;
    letter-spacing: 4px;
    color: var(--ink);
  }
  .contact-title {
    margin-top: 4px;
    font-size: 15px;
    line-height: 1.1;
    letter-spacing: 3px;
    color: var(--accent-red);
  }
  .contact-phone {
    margin-top: 16px;
    font-size: 15px;
    line-height: 1.1;
    letter-spacing: 4px;
    color: var(--ink);
  }
  .contact-email {
    margin-top: 4px;
    font-size: 15px;
    line-height: 1.1;
    letter-spacing: 2.5px;
    color: var(--ink);
  }
</style>
</head>
<body>
  <main class="canvas">
    <section class="card card--front">
      <div class="card-texture" role="img" aria-label="Cracked windscreen glass texture in silver-grey tones"></div>
      <div class="brand">
        <div class="brand-name">PANE RANGERS</div>
        <div class="brand-specialty">GLASS CRACK REPAIR SPECIALISTS</div>
        <div class="brand-tagline">QUICKER CHEAPER BETTER</div>
      </div>
    </section>

    <section class="card card--back">
      <div class="card-texture" role="img" aria-label="Shattered glass texture in pale sea-green tones"></div>
      <div class="contact-band"></div>
      <div class="contact">
        <div class="contact-name">DARREN WHITLOCK</div>
        <div class="contact-title">OWNER / GLASS REPAIR TECHNICIAN</div>
        <div class="contact-phone">0438 162 705</div>
        <div class="contact-email">DWHITLOCK@PANERIDERSWA.COM.AU</div>
      </div>
    </section>
  </main>
</body>
</html>
```